Business Card Design needed for start up company Pelmora

In need of a new business card designed for a start up company based in Sydney, Pelmora is a new start up innovative Company, our mission it to make property accessible for everyday Australian and to become the leading Real Estate platform in Australia. We want it to be fresh and clean.

Industry/Entity Type

Financial

Contact Information for Business Card

Section for Name
Section for Title

PELMORA - Keys Within Reach
Mobile:
Direct:

Font styles to use
Sans Serif

Colors
33a6d7
0692cd
0255a3
ffffff

Requirements
Must have
• Logo, all business card details

```html
<!DOCTYPE html>
<html lang="en">
<head>
<meta charset="utf-8">
<title>Pelmora Business Card</title>
<link href="https://fonts.googleapis.com/css2?family=Lato:wght@300;400;700;900&display=swap" rel="stylesheet">
<style>
  :root {
    --page-bg: #e9ebee;
    --card-clear: #f1f3f5;
    --panel-deep: #0a1c4e;
    --panel-mid: #1e3567;
    --panel-soft: #2f4a7e;
    --accent-sky: #33a6d7;
    --accent-blue: #0692cd;
    --brand-navy: #0f2a4f;
    --brand-blue: #0255a3;
    --text-light: #e6eaf2;
    --text-muted: #c9d1e0;
  }
  * { margin: 0; padding: 0; box-sizing: border-box; }
  html, body {
    width: 1200px; height: 970px; overflow: hidden;
    background: var(--page-bg);
    font-family: "Lato", sans-serif;
  }
  .card {
    position: absolute; left: 80px; top: 188px;
    width: 1040px; height: 594px;
    border-radius: 26px; overflow: hidden;
    background: linear-gradient(160deg, #f8f9fb 0%, var(--card-clear) 55%, #e4e8ec 100%);
    box-shadow: 0 14px 40px rgba(20, 30, 60, 0.18);
  }
  .card-shape { position: absolute; inset: 0; }
  .name-tab {
    position: absolute; left: -30px; top: 88px;
    width: 60px; height: 64px; border-radius: 50%;
    background: var(--accent-blue);
  }
  .holder { position: absolute; left: 46px; top: 88px; color: var(--text-light); }
  .holder-name { font-weight: 700; font-size: 36px; letter-spacing: 0.5px; line-height: 1; }
  .holder-title { font-weight: 400; font-size: 29px; line-height: 1.1; margin-top: 2px; }
  .address {
    position: absolute; left: 48px; top: 288px;
    color: var(--text-muted); font-size: 26px; line-height: 32px; font-weight: 400;
  }
  .contacts { position: absolute; left: 46px; top: 380px; list-style: none; }
  .contact {
    display: flex; align-items: center; gap: 14px;
    color: var(--text-muted); font-size: 28px; height: 37px;
  }
  .contact.email { font-size: 26px; }
  .contact-icon {
    width: 32px; height: 32px; border-radius: 50%;
    background: var(--accent-blue); display: flex; align-items: center; justify-content: center;
    flex: none;
  }
  .brand { position: absolute; left: 500px; top: 232px; width: 500px; }
  .brand-row { display: flex; align-items: center; gap: 18px; }
  .brand-dot { width: 120px; height: 120px; border-radius: 50%; background: var(--brand-blue); flex: none; }
  .brand-name { font-weight: 900; font-size: 72px; color: var(--brand-navy); letter-spacing: -1px; line-height: 1; }
  .brand-tagline {
    text-align: right; font-weight: 700; font-size: 26px; color: var(--brand-navy);
    margin-top: -14px; padding-right: 2px;
  }
</style>
</head>
<body>
  <article class="card">
    <svg class="card-shape" viewBox="0 0 1040 594" width="1040" height="594" aria-hidden="true">
      <defs>
        <linearGradient id="panelFill" x1="0" y1="0" x2="1" y2="1">
          <stop offset="0" stop-color="#2b4476"/>
          <stop offset="0.45" stop-color="#1a3062"/>
          <stop offset="0.8" stop-color="#0a1c4e"/>
          <stop offset="1" stop-color="#24406f"/>
        </linearGradient>
      </defs>
      <path d="M0,0 H540 Q430,297 540,594 H0 Z" fill="url(#panelFill)"/>
      <path d="M540,0 Q430,297 540,594" fill="none" stroke="#0692cd" stroke-width="6"/>
      <path d="M548,0 Q442,297 548,594" fill="none" stroke="#33a6d7" stroke-width="2" opacity="0.6"/>
    </svg>

    <div class="name-tab"></div>
    <header class="holder">
      <h1 class="holder-name">LIAM CARTER</h1>
      <p class="holder-title">Managing Director</p>
    </header>

    <address class="address">PO BOX 418 Harbour Lane<br>Sydney NSW, Australia</address>

    <ul class="contacts">
      <li class="contact">
        <span class="contact-icon">
          <svg width="14" height="20" viewBox="0 0 14 20"><rect x="1" y="1" width="12" height="18" rx="2" fill="none" stroke="#fff" stroke-width="2"/><rect x="4" y="4" width="6" height="7" fill="#fff"/></svg>
        </span>
        <span>0412 555 018</span>
      </li>
      <li class="contact">
        <span class="contact-icon">
          <svg width="20" height="16" viewBox="0 0 20 16"><path d="M1,6 Q10,-1 19,6 L16,8 L13,5 H7 L4,8 Z" fill="#fff"/><rect x="4" y="8" width="12" height="7" rx="1.5" fill="#fff"/></svg>
        </span>
        <span>02 5550 1234</span>
      </li>
      <li class="contact email">
        <span class="contact-icon">
          <svg width="18" height="13" viewBox="0 0 18 13"><rect x="1" y="1" width="16" height="11" fill="none" stroke="#fff" stroke-width="1.8"/><path d="M1,1 L9,7 L17,1" fill="none" stroke="#fff" stroke-width="1.8"/></svg>
        </span>
        <span>liam@pelmora.com.au</span>
      </li>
    </ul>

    <section class="brand">
      <div class="brand-row">
        <span class="brand-dot"></span>
        <span class="brand-name">PELMORA</span>
      </div>
      <p class="brand-tagline">Keys Within Reach</p>
    </section>
  </article>
</body>
</html>
```